" ATENDEMOS CLIENTES DE BALCÃO PARA VENDA DE PEÇAS E PNEUS DA LINHA LEVE + CAMIONETES NACIONAIS E IMPORTADOS. CONTAMOS COM UM CENTRO AUTOMOTIVO DE GRANDE PORTE PARA EXECUTAR SERVIÇOS MECÂNICOS DE REVISÃO E MANUTENÇÃO CORRETIVA E PREVENTIVA ( ALINHAMENTO, BALANCEAMENTO, MONTAGEM DE PNEUS, SUSPENSÃO, FREIOS, CAMBIO MANUAL E AUTOMATIZADO, INJEÇÃO ELETRÔNICA, REPARO DE MOTOR E CABEÇOTES, SISTEMA DE DIREÇÃO ). "

```html
<!DOCTYPE html>
<html lang="pt-BR">
<head>
<meta charset="UTF-8">
<title>Velotec – Cartão de Visita</title>
<link rel="stylesheet" href="https://fonts.googleapis.com/css2?family=Saira:wght@600;800&family=Roboto:wght@400;500&display=swap">
<style>
  :root {
    --page-bg: #1d222a;
    --navy: #16202c;
    --red: #e3242b;
    --white: #ffffff;
    --paper: #f7f7f8;
    --ink: #2a2f36;
    --muted: #8a9099;
    --swoosh: #ececee;
  }
  * { box-sizing: border-box; margin: 0; padding: 0; }
  html, body { width: 1200px; height: 1200px; overflow: hidden; }
  body {
    background: var(--page-bg);
    font-family: "Roboto", Arial, sans-serif;
    position: relative;
  }
  .card {
    position: absolute;
    width: 700px;
    height: 400px;
    border-radius: 26px;
    overflow: hidden;
  }
  .card-band {
    position: absolute;
    left: 0; right: 0; bottom: 0;
    height: 14px;
    background: var(--red);
  }
  .card-front { left: 380px; top: 150px; background: var(--navy); }
  .card-back { left: 120px; top: 640px; background: var(--paper); }

  .brand {
    position: absolute;
    display: flex;
    flex-direction: column;
    align-items: flex-end;
  }
  .brand-row { display: flex; align-items: center; gap: 14px; }
  .brand-dot { width: 18px; height: 18px; border-radius: 50%; background: var(--red); }
  .brand-name {
    font-family: "Saira", Arial, sans-serif;
    font-weight: 800;
    letter-spacing: 2px;
    line-height: 1;
  }
  .brand-tagline {
    font-family: "Saira", Arial, sans-serif;
    font-weight: 600;
    text-transform: uppercase;
    letter-spacing: 3px;
  }
  .card-front .brand { right: 90px; top: 140px; }
  .card-front .brand-name { font-size: 84px; color: var(--white); }
  .card-front .brand-tagline { font-size: 18px; color: var(--white); margin-top: 8px; }

  .card-back .brand { left: 50px; top: 110px; align-items: flex-start; }
  .card-back .brand-row { gap: 10px; }
  .card-back .brand-dot { width: 12px; height: 12px; }
  .card-back .brand-name { font-size: 46px; color: var(--navy); }
  .card-back .brand-tagline { font-size: 11px; color: var(--ink); margin: 6px 0 0 22px; letter-spacing: 2px; }

  .swoosh { position: absolute; left: 0; top: 0; }
  .corner-wedge { position: absolute; right: 0; bottom: 0; }

  .divider {
    position: absolute;
    left: 350px;
    top: 40px;
    width: 2px;
    height: 290px;
    background: var(--ink);
  }
  .contact {
    position: absolute;
    left: 380px;
    top: 40px;
    list-style: none;
    color: var(--ink);
  }
  .contact li { display: flex; align-items: center; gap: 14px; font-size: 15px; }
  .contact .person { align-items: flex-start; margin-bottom: 30px; }
  .contact .person-name { font-size: 20px; font-weight: 500; letter-spacing: 1px; }
  .contact .person-role { font-size: 10px; color: var(--muted); letter-spacing: 1px; margin-top: 3px; }
  .contact li + li { margin-top: 14px; }
  .icon { width: 22px; height: 22px; flex: none; }
</style>
</head>
<body>

  <section class="card card-front">
    <div class="brand">
      <div class="brand-row">
        <span class="brand-dot"></span>
        <span class="brand-name">VELOTEC</span>
      </div>
      <span class="brand-tagline">Centro Automotivo</span>
    </div>
    <div class="card-band"></div>
  </section>

  <section class="card card-back">
    <svg class="swoosh" width="700" height="400" viewBox="0 0 700 400">
      <path d="M0 250 C 180 170, 420 180, 700 280 L700 300 C 420 205, 180 200, 0 275 Z" fill="var(--swoosh)"/>
    </svg>
    <svg class="corner-wedge" width="360" height="84" viewBox="0 0 360 84">
      <path d="M0 84 C 120 74, 260 49, 360 14 L360 84 Z" fill="var(--red)"/>
    </svg>

    <div class="brand">
      <div class="brand-row">
        <span class="brand-dot"></span>
        <span class="brand-name">VELOTEC</span>
      </div>
      <span class="brand-tagline">Centro Automotivo</span>
    </div>

    <div class="divider"></div>

    <ul class="contact">
      <li class="person">
        <svg class="icon" viewBox="0 0 24 24"><rect width="24" height="24" rx="4" fill="var(--red)"/><circle cx="12" cy="9" r="4" fill="#fff"/><path d="M5 20c1-4 4-6 7-6s6 2 7 6z" fill="#fff"/></svg>
        <div>
          <div class="person-name">NOME SOBRENOME</div>
          <div class="person-role">CARGO</div>
        </div>
      </li>
      <li>
        <svg class="icon" viewBox="0 0 24 24"><circle cx="12" cy="12" r="12" fill="var(--red)"/><rect x="6" y="8" width="12" height="9" rx="1" fill="none" stroke="#fff" stroke-width="1.6"/><path d="M6 8l6 5 6-5" fill="none" stroke="#fff" stroke-width="1.6"/></svg>
        <span>email.empresa@com.br</span>
      </li>
      <li>
        <svg class="icon" viewBox="0 0 24 24"><circle cx="12" cy="12" r="12" fill="var(--red)"/><circle cx="12" cy="12" r="6.5" fill="none" stroke="#fff" stroke-width="1.5"/><ellipse cx="12" cy="12" rx="3" ry="6.5" fill="none" stroke="#fff" stroke-width="1.3"/><path d="M5.5 12h13" stroke="#fff" stroke-width="1.3"/></svg>
        <span>www.site.com.br</span>
      </li>
      <li>
        <svg class="icon" viewBox="0 0 24 24"><circle cx="12" cy="12" r="12" fill="var(--red)"/><path d="M8 6l2.5 0 1 3-1.5 1.2c.8 1.6 2 2.8 3.6 3.6L14.8 12.3l3 1V16c0 .8-.7 1.5-1.5 1.4C10.8 17 7 13.2 6.6 7.6 6.5 6.7 7.2 6 8 6z" fill="#fff"/></svg>
        <span>+ 55 (99) 0000-0000</span>
      </li>
      <li>
        <svg class="icon" viewBox="0 0 24 24"><circle cx="12" cy="12" r="12" fill="var(--red)"/><path d="M12 5a4.5 4.5 0 0 0-4.5 4.5C7.5 13 12 19 12 19s4.5-6 4.5-9.5A4.5 4.5 0 0 0 12 5z" fill="#fff"/><circle cx="12" cy="9.5" r="1.7" fill="var(--red)"/></svg>
        <span>Rua do Projeto, 999</span>
      </li>
    </ul>
    <div class="card-band"></div>
  </section>

</body>
</html>
```